■依頼の目的/概要
鶏白湯塩ラーメンのポスター作成お願いします!

■依頼詳細
鶏白湯塩ラーメンのポスターを作成お願いします。
値段は780円です。

デザインについては特に、指定はありません。
A1のポスターです。

鶏白湯塩ラーメンについて

鶏白湯スープにじっくり時間をかけて熟成させた自家製塩タレを合わせ、アクセントにアオサを使用しました。
(こちらの文章を入れて欲しいです。)

写真はURLからダウンロードお願いします。

http://filebako.example/dl/7a1c93e0b5d2f4c8a6e1027b3d9f5c4e8a1b6d20

お店のイメージです。
こちらのお店の物になります。

https://gurumemo.example/fukuoka/B7002/B700209/51178364/

https://www.tomobook.example/torisoba.hakata/
http://filebako.example/dl/3e8d21f6c0a94b7e5d13a8f2c6b0e974d1a5c3b8

おそくなりましたこちらからダウンロードお願いしいます。
再度アップしました。こちらからダウンロードできますか?
http://filebako.example/dl/c5b07e3a91d6f2e48a0c7b15d3e9f6a2b4c81d07

とても素晴らしいデザインありがとうございます!

提案ありがとうございました!

```html
<!DOCTYPE html>
<html lang="ja">
<head>
<meta charset="utf-8">
<title>鶏白湯 塩ラーメン</title>
<link rel="stylesheet" href="https://fonts.googleapis.com/css2?family=Yuji+Syuku&family=Noto+Serif+JP:wght@600;900&display=swap">
<style>
  :root {
    --wood-light: #b98a5c;
    --wood-mid: #8a5a35;
    --wood-dark: #3a2214;
    --ink: #16100c;
    --accent-red: #c8161d;
    --broth: #efe9dd;
    --paper: #ffffff;
  }
  * { margin: 0; padding: 0; box-sizing: border-box; }
  html, body { width: 849px; height: 1200px; overflow: hidden; }
  body { background: var(--wood-dark); }
  .poster {
    position: relative;
    width: 849px;
    height: 1200px;
    overflow: hidden;
    font-family: "Noto Serif JP", serif;
    color: var(--ink);
  }
  .poster__backdrop {
    position: absolute; inset: 0;
    background: linear-gradient(100deg, var(--wood-dark) 0%, var(--wood-mid) 35%, var(--wood-light) 70%, var(--wood-mid) 100%);
  }
  .poster__dish {
    position: absolute;
    left: -40px; top: 640px;
    width: 930px; height: 620px;
    border-radius: 50% 50% 0 0 / 38% 38% 0 0;
    background: radial-gradient(ellipse at 50% 45%, var(--broth) 0%, #ddd4c2 55%, #a99a82 80%, var(--wood-dark) 100%);
  }
  .headline {
    position: absolute;
    writing-mode: vertical-rl;
    font-weight: 900;
    line-height: 1;
  }
  .headline--soup {
    right: 30px; top: 42px;
    font-family: "Yuji Syuku", serif;
    font-size: 120px;
    letter-spacing: -8px;
  }
  .headline--soup .headline__mark { color: var(--accent-red); }
  .headline--dish {
    right: 165px; top: 100px;
    font-size: 160px;
    letter-spacing: -38px;
  }
  .description {
    position: absolute;
    right: 382px; top: 60px;
    writing-mode: vertical-rl;
    font-size: 26px;
    font-weight: 600;
    line-height: 2.3;
    letter-spacing: 0;
  }
  .price {
    position: absolute;
    left: 60px; top: 505px;
    font-weight: 900;
    font-size: 76px;
    line-height: 1;
    padding: 10px 18px;
    background: var(--paper);
    border-radius: 6px;
    transform: rotate(-2deg);
  }
  .price__unit { font-size: 44px; }
  .brand {
    position: absolute;
    left: 0; right: 0; bottom: 40px;
    text-align: center;
    font-size: 40px;
    font-weight: 900;
    letter-spacing: 1px;
    color: var(--ink);
  }
</style>
</head>
<body>
  <main class="poster">
    <div class="poster__backdrop" role="img" aria-label="暗い木目のテーブル背景"></div>
    <div class="poster__dish" role="img" aria-label="鶏白湯塩ラーメンの写真：白濁スープ、チャーシュー、白髪ねぎ、アオサ、箸で持ち上げた麺"></div>

    <h1 class="headline headline--soup"><span class="headline__mark">鶏</span>白湯</h1>
    <h2 class="headline headline--dish">塩ラーメン</h2>

    <p class="description">鶏白湯スープにじっくり時間をかけて<br>熟成させた自家製塩タレを合わせ、<br>アクセントにアオサを使用しました。</p>

    <p class="price">780<span class="price__unit">円</span></p>

    <p class="brand">KOKKO NOODLE</p>
  </main>
</body>
</html>
```